My name is Tomas Verenda, and I have done business with your company several times. I need a business card to represent my business, I own a company by the name of BELOMI Suntan Lotion & Sunscreen.
My requirements are as follow: My company logo in the brightest gold possible, on a black, grainy (sandy) background, with shading around the each element. With the company name in gold, a stylized coconut trees, and some type of wave graphic in gold. "A product of the USA, Staten Island, NY"
"For comments, suggestion, or ordering please contact us at:
belomi42@nexamail.test"

"BELOMI™ Tanning Lotion & Sunscreen―Crafted with Care"

Belomi Tanning Lotion & Sunscreen is the most extraordinary and innovative sun tanning product to emerge in several generations. The constituents of this product are formidable substances that protect the skin against the aftermath of sun exposure−before you exposed yourself to the sun’s rays. The Aloe Vera in this product, along with other oils and cream, are specifically manufactured to lessen the symptoms of extended exposure to the sun. Belomi is designed to provide a Broad Spectrum Protection (50) that assist in the reduction of (UVA) and (UVB) radiation to create a magnificent sun-absorbing, long-lasting, deep dark bronzing experience.
Thank you,
Tomas Verenda
tomastverenda@postline.test

Target Market(s)

Sunscreen

Industry/Entity Type

Business

Contact Information for Business Card

BELOMI™ Tanning Lotion and Sunscreen
Crafted with Care

Belomi Tanning Lotion is the most extraordinary and innovative sun tanning product to emerge in several generations. The constituents of this product are formidable substances that protect the skin against the aftermath of sun exposure−before you exposed yourself to the sun’s rays. The Aloe Vera, in this product, along with other oils and cream, are specifically manufactured to lessen the symptoms of extended exposure to the sun. Belomi protects your skin from dehydration and treat your skin with the products we apply to ourselves after a sunburn−before the sun tanning process begins. Belomi is designed to provide a Broad Spectrum Protection (50) that assist in the reduction of (UVA) and (UVB) radiation to create a magnificent sun-absorbing, long-lasting, deep dark bronzing experience.

Colors
fece3e
acd136

Requirements
Must have
• Black Card Stock with grainy surface, Gold Logo, stylized Coconut Palm Tree, Company Name, email address, and NYC location.
• Modern Layout with Modern fonts and graphics

```html
<!DOCTYPE html>
<html lang="en">
<head>
<meta charset="utf-8">
<title>BELOMI Business Card</title>
<link rel="stylesheet" href="https://fonts.googleapis.com/css2?family=Cinzel:wght@700&family=Open+Sans:wght@600;700&family=Montserrat:wght@400;700&display=swap">
<style>
  :root {
    --stage: #2b2b2b;
    --card: #0b0b0b;
    --card-edge: #1a1a1a;
    --gold: #e9b949;
    --gold-bright: #fece3e;
    --gold-pale: #f6efd0;
    --gold-deep: #b07a1c;
    --white: #f4f4f4;
    --muted: #cfcfcf;
  }
  * { margin: 0; padding: 0; box-sizing: border-box; }
  html, body { width: 1200px; height: 900px; overflow: hidden; }
  body { background: var(--stage); position: relative; font-family: "Montserrat", sans-serif; }

  .card {
    position: absolute;
    width: 540px; height: 300px;
    border-radius: 22px;
    background:
      radial-gradient(circle at 1px 1px, rgba(255,255,255,.05) 1px, transparent 1.5px) 0 0 / 4px 4px,
      radial-gradient(ellipse at 40% 30%, var(--card-edge), var(--card) 70%);
    box-shadow: 0 18px 40px rgba(0,0,0,.55);
    overflow: hidden;
  }
  .card--front { left: 90px; top: 110px; }
  .card--back { left: 570px; top: 490px; }

  .brand { display: flex; flex-direction: column; align-items: center; }
  .brand__mark {
    width: 78px; height: 78px; border-radius: 50%;
    background: var(--gold);
    box-shadow: 0 4px 10px rgba(0,0,0,.6);
  }
  .brand__name {
    font-family: "Cinzel", serif; font-weight: 700;
    color: var(--white); font-size: 50px; letter-spacing: 1px;
    line-height: 1; margin-top: 8px;
  }
  .brand__tm { font-size: 0.32em; vertical-align: super; }
  .brand__tagline {
    font-family: "Open Sans", sans-serif; font-weight: 700;
    color: var(--white); font-size: 14px; letter-spacing: .3px; margin-top: 2px;
  }
  .brand__values {
    font-family: "Open Sans", sans-serif; font-weight: 600;
    color: var(--gold); font-size: 10px; letter-spacing: .5px; margin-top: 8px;
  }

  .card--front .brand { position: absolute; left: 0; right: 0; top: 52px; }

  .card--back .brand { position: absolute; left: 42px; top: 30px; }
  .card--back .brand__mark { width: 62px; height: 62px; }
  .card--back .brand__name { font-size: 40px; }
  .card--back .brand__tagline { font-size: 11px; }

  .person { position: absolute; left: 46px; top: 188px; }
  .person__name { color: var(--gold-bright); font-weight: 700; font-size: 21px; }
  .person__role { color: var(--muted); font-size: 9px; letter-spacing: 1px; margin-top: 2px; }
  .person__address { color: var(--muted); font-size: 9px; letter-spacing: 1px; line-height: 1.5; margin-top: 14px; }

  .contact { position: absolute; left: 262px; top: 206px; list-style: none; }
  .contact__item {
    display: flex; align-items: center; gap: 10px;
    color: var(--muted); font-size: 9px; letter-spacing: 1px; margin-bottom: 6px;
  }
  .contact__icon { width: 11px; height: 11px; flex: none; }

  .palm-art {
    position: absolute; left: 360px; top: 0;
    width: 150px; height: 185px;
    background: linear-gradient(160deg, var(--gold-pale) 0%, var(--gold) 55%, var(--gold-deep) 100%);
    border-radius: 50% 50% 14% 14% / 38% 38% 8% 8%;
    opacity: .9;
  }
  .sand-hill { position: absolute; right: 0; bottom: 0; }
</style>
</head>
<body>

  <section class="card card--front" aria-label="Card front">
    <div class="brand">
      <div class="brand__mark"></div>
      <div class="brand__name">BELOMI<span class="brand__tm">™</span></div>
      <div class="brand__tagline">SUNTAN LOTION &amp; SUNSCREEN</div>
      <div class="brand__values">NEW · SOPHISTICATE · VELVETY · SMOOTH</div>
    </div>
  </section>

  <section class="card card--back" aria-label="Card back">
    <div class="palm-art" role="img" aria-label="Gold and white engraved coconut palm tree"></div>
    <svg class="sand-hill" width="140" height="70" viewBox="0 0 140 70" aria-hidden="true">
      <defs>
        <linearGradient id="sand" x1="0" y1="0" x2="1" y2="1">
          <stop offset="0" stop-color="#fece3e"/>
          <stop offset="1" stop-color="#b07a1c"/>
        </linearGradient>
      </defs>
      <path d="M0 70 Q30 8 140 2 L140 70 Z" fill="url(#sand)"/>
    </svg>

    <div class="brand">
      <div class="brand__mark"></div>
      <div class="brand__name">BELOMI<span class="brand__tm">™</span></div>
      <div class="brand__tagline">SUNTAN LOTION &amp; SUNSCREEN</div>
    </div>

    <div class="person">
      <div class="person__name">Tomas Verenda</div>
      <div class="person__role">Manager</div>
      <div class="person__address">A Product of the USA<br>Staten Island, NY 10301</div>
    </div>

    <ul class="contact">
      <li class="contact__item">
        <svg class="contact__icon" viewBox="0 0 12 12" aria-hidden="true"><rect x="3" y="1" width="6" height="10" rx="1" fill="none" stroke="#fece3e" stroke-width="1.4"/></svg>
        555 0148 220
      </li>
      <li class="contact__item">
        <svg class="contact__icon" viewBox="0 0 12 12" aria-hidden="true"><rect x="1" y="2" width="10" height="8" fill="none" stroke="#fece3e" stroke-width="1.3"/><path d="M1 2 L6 7 L11 2" fill="none" stroke="#fece3e" stroke-width="1.3"/></svg>
        belomi42@nexamail.test
      </li>
      <li class="contact__item">
        <svg class="contact__icon" viewBox="0 0 12 12" aria-hidden="true"><circle cx="6" cy="6" r="5" fill="#fece3e"/><path d="M1 6 H11 M6 1 V11" stroke="#0b0b0b" stroke-width="1"/></svg>
        www.belomi.test
      </li>
    </ul>
  </section>

</body>
</html>
```